Tessa the Musical Poster HS Theatre

Our students have started on a design for Tessa the Musical and we need some help bringing the professional touch to the design. We were hoping a designer could work with the colors and fonts to make a more professional layout and a poster that conveys this message, but in a more polished way. This musical is based on the Owen Tarrask novel, and was imagined as our actress in her prom dress seeing her reflection with blood on her face. It was decided that the picture with the blood was too graphic for our HS audience, and we made the negative image version, which we like much better. The main help we need now is making the background, the fonts and the overall color scheme to work together. We want something darker and with more shadows, but with the text much more legible from a distance. The title needs to be larger, and the other info is necessary, but it is hard to read. I have included all the files used to make this draft version. Feel free to substitute and all fonts, including the title if you think it would look better.

Target Market(s)

High School Students

Industry/Entity Type

Education

Requirements
Must have
• All the included text
Should not have
• Too much violence

```html
<!DOCTYPE html>
<html lang="en">
<head>
<meta charset="utf-8">
<title>Tessa the Musical – Cedar Bluff Theater</title>
<link href="https://fonts.googleapis.com/css2?family=Amatic+SC:wght@700&family=Cabin:wght@400;700&family=Caveat:wght@500&family=Montserrat:wght@600&display=swap" rel="stylesheet">
<style>
  :root {
    --blood: #b30000;
    --crimson: #8a0000;
    --deep: #2a0000;
    --ink: #000000;
    --pale: #f4dde2;
    --white: #ffffff;
  }
  html, body {
    margin: 0;
    padding: 0;
    width: 840px;
    height: 1200px;
    overflow: hidden;
    background: var(--ink);
  }
  .poster {
    position: relative;
    width: 840px;
    height: 1200px;
    overflow: hidden;
    background:
      radial-gradient(ellipse 70% 55% at 55% 18%, #c20000 0%, var(--crimson) 40%, var(--deep) 80%, #140000 100%);
    font-family: "Cabin", sans-serif;
    color: var(--white);
  }
  .presenter {
    position: absolute;
    left: 33px;
    top: 34px;
    margin: 0;
    font-size: 27px;
    font-weight: 700;
    letter-spacing: -0.5px;
  }
  .portrait {
    position: absolute;
    left: 150px;
    top: 320px;
    width: 510px;
    height: 470px;
    border-radius: 48% 48% 0 0;
    background: radial-gradient(ellipse 50% 55% at 50% 45%, #c98a5a 0%, #7a2a10 45%, #3a0a04 80%, rgba(40,0,0,0) 100%);
  }
  .title {
    position: absolute;
    left: 0;
    top: 70px;
    width: 840px;
    margin: 0;
    text-align: center;
    font-family: "Amatic SC", cursive;
    font-weight: 700;
    font-size: 300px;
    line-height: 1;
    color: var(--pale);
    letter-spacing: -4px;
    transform: scaleY(1.3);
    transform-origin: top center;
    opacity: 0.93;
  }
  .subtitle {
    position: absolute;
    left: 493px;
    top: 352px;
    width: 190px;
    height: 46px;
    margin: 0;
  }
  .subtitle-band {
    position: absolute;
    left: 0;
    bottom: 0;
    width: 100%;
    height: 30px;
    background: #c41a1a;
  }
  .subtitle-text {
    position: relative;
    padding-left: 6px;
    font-family: "Caveat", cursive;
    font-weight: 500;
    font-size: 42px;
    line-height: 46px;
    color: var(--pale);
  }
  .tickets {
    position: absolute;
    left: 656px;
    top: 650px;
    width: 184px;
    height: 117px;
    background: var(--blood);
    box-sizing: border-box;
    padding: 17px 18px 0 0;
    text-align: right;
  }
  .tickets-line {
    margin: 0;
    font-size: 16px;
    font-weight: 700;
    line-height: 20px;
  }
  .vendor {
    margin: 10px 0 0;
    font-size: 26px;
    font-weight: 700;
    line-height: 1;
  }
  .date-band {
    position: absolute;
    left: 0;
    top: 790px;
    width: 840px;
    height: 67px;
    background: var(--ink);
    display: flex;
    align-items: center;
    justify-content: center;
  }
  .date {
    margin: 0;
    font-family: "Montserrat", sans-serif;
    font-weight: 600;
    font-size: 50px;
    letter-spacing: 0.5px;
  }
  .reflection {
    position: absolute;
    left: 0;
    top: 857px;
    width: 840px;
    height: 343px;
    background:
      radial-gradient(ellipse 40% 60% at 45% 40%, #d01010 0%, #a00000 45%, rgba(80,0,0,0.6) 75%, rgba(20,0,0,0.9) 100%),
      linear-gradient(180deg, #b00000 0%, #5a0000 100%);
  }
  .credits {
    position: absolute;
    right: 15px;
    top: 925px;
    text-align: right;
    font-size: 20px;
    font-weight: 700;
    line-height: 26px;
  }
  .credits p { margin: 0; }
  .credits .group + .group { margin-top: 16px; }
  .warning {
    position: absolute;
    left: 56px;
    top: 1113px;
    width: 740px;
    margin: 0;
    font-size: 15.5px;
    line-height: 19.5px;
    font-weight: 400;
  }
  .warning strong { font-weight: 700; }
</style>
</head>
<body>
  <main class="poster">
    <div class="portrait" role="img" aria-label="Portrait photo of the lead actress, red hair, looking toward the viewer under red light"></div>

    <p class="presenter">Cedar Bluff Theater Present</p>

    <h1 class="title">TESSA</h1>
    <div class="subtitle">
      <span class="subtitle-band"></span>
      <span class="subtitle-text">the musical</span>
    </div>

    <aside class="tickets">
      <p class="tickets-line">Buy Tickets at</p>
      <p class="tickets-line">ridge.seatloop.com</p>
      <p class="vendor">SeatLoop</p>
    </aside>

    <div class="date-band">
      <p class="date">April 10th / 12th at 7:00 pm</p>
    </div>

    <div class="reflection" role="img" aria-label="Red negative-image reflection of the actress in her prom dress"></div>

    <section class="credits">
      <div class="group">
        <p>Book by Martin J. Ellery</p>
        <p>Based on the novel by Owen Tarrask</p>
      </div>
      <div class="group">
        <p>Music By Daniel Roarke</p>
        <p>Lyrics by Peter Halvorsen</p>
      </div>
    </section>

    <p class="warning"><strong>CONTENT WARNING:</strong> Tessa: The Musical is intended for mature audiences. This musical is rated PG-13. It includes depictions of bullying, violence and death, as well as mentions of menstruation, sexual assault, group and animal violence. This show will be using fog, fake blood and lights.</p>
  </main>
</body>
</html>
```